Horse related business entrepreneur needs a business card

I need a business card design for my horse related business. The enterprise is Copper Vale LLC and I have 3 businesses (headquartered at 2 locations): 1. property management where we rent horse stalls and apartments at a thoroughbred training center outside Ocala; 2. a medium sized transportation service in central Florida that sells horse bedding and removes used horse bedding from horse farms; and horse racing

```html
<!DOCTYPE html>
<html lang="en">
<head>
<meta charset="utf-8">
<title>Copper Vale LLC – Business Card</title>
<link href="https://fonts.googleapis.com/css2?family=Cinzel:wght@400;600&family=Tinos&family=Crimson+Text:ital@1&family=Roboto:wght@400&display=swap" rel="stylesheet">
<style>
  :root {
    --backdrop: #2b2b2b;
    --teal: #035a73;
    --copper: #e06f45;
    --paper: #ffffff;
    --ink-light: #ffffff;
    --ink-grey: #555a5e;
    --rule-light: rgba(255,255,255,0.55);
  }
  * { margin: 0; padding: 0; box-sizing: border-box; }
  html, body { width: 1125px; height: 1200px; overflow: hidden; }
  body { background: var(--backdrop); position: relative; }

  .card {
    position: absolute;
    left: 150px;
    width: 826px;
    height: 471px;
  }
  .card--front { top: 98px; background: var(--teal); color: var(--ink-light); }
  .card--back { top: 631px; background: var(--paper); }

  .holder {
    position: absolute;
    right: 52px;
    top: 40px;
    text-align: right;
    font-family: "Cinzel", serif;
    font-weight: 600;
    line-height: 1;
  }
  .holder__name { font-size: 36px; letter-spacing: 0.5px; }
  .holder__title { font-size: 22px; margin-top: 4px; }

  .contact-list {
    position: absolute;
    left: 50px;
    top: 255px;
    list-style: none;
    font-family: "Tinos", serif;
    font-size: 19px;
  }
  .contact-list li {
    display: flex;
    align-items: center;
    height: 26px;
  }
  .contact-list svg { width: 18px; height: 18px; margin-right: 13px; fill: var(--ink-light); }

  .front-rule {
    position: absolute;
    left: 50px;
    right: 50px;
    top: 377px;
    border-top: 1px solid var(--rule-light);
  }
  .company-line {
    position: absolute;
    left: 50px;
    top: 393px;
    font-family: "Tinos", serif;
    font-size: 19px;
  }

  .farm-name {
    position: absolute;
    left: 0; right: 0;
    top: 242px;
    text-align: center;
    font-family: "Cinzel", serif;
    font-weight: 600;
    font-size: 40px;
    letter-spacing: 3px;
    color: var(--teal);
    line-height: 1;
  }
  .farm-rule {
    position: absolute;
    left: 270px;
    width: 285px;
    top: 232px;
    border-top: 1.5px solid var(--copper);
  }
  .farm-place {
    position: absolute;
    left: 0; right: 0;
    top: 296px;
    text-align: center;
    font-family: "Crimson Text", serif;
    font-style: italic;
    font-size: 28px;
    color: var(--copper);
    line-height: 1;
  }
  .addresses {
    position: absolute;
    left: 0; right: 0;
    top: 380px;
    text-align: center;
    font-family: "Roboto", sans-serif;
    font-size: 19px;
    line-height: 27px;
    color: var(--ink-grey);
    font-style: normal;
  }
</style>
</head>
<body>

<section class="card card--front">
  <div class="holder">
    <div class="holder__name">Dana Whitcombe</div>
    <div class="holder__title">Owner</div>
  </div>

  <ul class="contact-list">
    <li>
      <svg viewBox="0 0 24 24" aria-hidden="true"><path d="M6.6 10.8a15 15 0 0 0 6.6 6.6l2.2-2.2c.3-.3.7-.4 1-.2 1.1.4 2.3.6 3.6.6.6 0 1 .4 1 1V20c0 .6-.4 1-1 1A17 17 0 0 1 3 4c0-.6.4-1 1-1h3.5c.6 0 1 .4 1 1 0 1.3.2 2.5.6 3.6.1.3 0 .7-.2 1z"/></svg>
      (434) 555-0148
    </li>
    <li>
      <svg viewBox="0 0 24 24" aria-hidden="true"><path d="M6 3h12v5H6z M3 9h18v9h-3v3H6v-3H3z M8 15v4h8v-4z"/></svg>
      (434) 555-0172
    </li>
    <li>
      <svg viewBox="0 0 24 24" aria-hidden="true"><path d="M2 5h20v14H2z M4 7v.4l8 5.3 8-5.3V7z" fill-rule="evenodd"/></svg>
      dana@coppervale.com
    </li>
    <li>
      <svg viewBox="0 0 24 24" aria-hidden="true"><circle cx="12" cy="12" r="10"/><path d="M8 6c2 1 1 3 3 4s1 3-1 3-2 3 0 5c-3-1-5-4-5-6s1-5 3-6zm8 3c1 1 3 1 3 4s-2 5-4 5c1-2 2-3 0-4s0-3 1-5z" fill="#035a73"/></svg>
      www.coppervale.com
    </li>
  </ul>

  <div class="front-rule"></div>
  <p class="company-line">Copper Vale LLC (an equine conglomerate)</p>
</section>

<section class="card card--back">
  <div class="farm-rule"></div>
  <h1 class="farm-name">Copper Vale Farm</h1>
  <p class="farm-place">Morriston FL</p>
  <address class="addresses">
    1745 SE 152nd Lane, Morriston, FL 32668<br>
    2180 Willow Ridge Road, Charlottesville, VA 22903
  </address>
</section>

</body>
</html>
```